Marrowind Radio needs a functional Internet Radio App

We need a Internet Radio app design for IOS and Android,
Shoutcast/ Icecast Stream( SHOUTcast playlist (.pls) file or Icecast (.m3u) playlist file) Supported streams: AAC, AAC+, HE-AAC+.
Should supports TuneBasket, Virtual Dj, Wowza, Auto Dj
Here are some of the features we need you to include in the design:
1. Multi Stream player with Scheduling
2. Track Display
3. Track Sharing ( Chatterbox and other)
4. Album Cover display( automatic cover retrieval base on track)
5.Track Purchases ( Plunkr and Brivex )
6.Push Notification( Geo-localize outgoing data and schedule messages)
7. News, Podcasts and Videos ( Live Feed)
8. Alarms
9. Incorporate "Dedications" ( Listeners love to see when their message is published in real time)
10.Ad management ( management system for the app)
11.Listeners should be able to 'Skip song'
12. Database for music

Target Market(s)

Everyone

Industry/Entity Type

Radio Station

Font styles to use
Decorative

Colors
3176b5
0355a3
85acd3
ffffff

Requirements
Must have
• 1.I need a functional app
• 2. Song Request
Nice to have
• N/A
Should not have
• Other Radio Station app design

```html
<!DOCTYPE html>
<html lang="en">
<head>
<meta charset="utf-8">
<title>Marrowind Radio – Live Feed</title>
<link rel="stylesheet" href="https://fonts.googleapis.com/css2?family=Montserrat:wght@400;500;600;700&display=swap">
<style>
  :root {
    --canvas: #e4e9f1;
    --white: #ffffff;
    --ink: #1c1c1c;
    --nav-blue: #0a3f94;
    --accent: #1a8ee0;
    --play: #1f86d6;
    --tab-bg: #1f1f1f;
    --tab-idle: #5b5b5b;
    --card-shadow: 0 4px 10px rgba(0, 0, 0, 0.18);
  }
  * { box-sizing: border-box; margin: 0; padding: 0; }
  html, body { width: 800px; height: 1200px; overflow: hidden; }
  body {
    background: var(--canvas);
    font-family: "Montserrat", sans-serif;
    color: var(--ink);
    position: relative;
  }
  .presentation-header {
    position: absolute; left: 0; top: 0; width: 800px; height: 64px;
    background: var(--white);
    display: flex; align-items: center; justify-content: space-between;
    padding: 0 18px;
  }
  .presentation-header .app-name { font-size: 26px; font-weight: 500; }
  .presentation-header .screen-count { font-size: 18px; font-weight: 400; }

  .phone {
    position: absolute; left: 100px; top: 92px; width: 600px; height: 1067px;
    background: var(--white); overflow: hidden;
  }
  .top-bar {
    position: absolute; left: 0; top: 0; width: 600px; height: 102px;
    background: var(--nav-blue); color: var(--white);
  }
  .status-bar {
    position: absolute; left: 10px; right: 10px; top: 6px; height: 22px;
    display: flex; align-items: center; justify-content: space-between;
    font-size: 17px; font-weight: 400;
  }
  .status-bar .signal { display: flex; align-items: center; gap: 6px; }
  .status-bar .battery { display: flex; align-items: center; gap: 5px; }
  .status-bar .time { position: absolute; left: 0; right: 0; text-align: center; pointer-events: none; }
  .screen-title {
    position: absolute; left: 0; right: 0; top: 143px; top: 52px;
    text-align: center; font-size: 24px; font-weight: 600; letter-spacing: 0.5px;
  }

  .feed-card {
    position: absolute; left: 26px; width: 548px;
    background: var(--white); box-shadow: var(--card-shadow);
  }
  .feed-card.first { top: 128px; height: 570px; }
  .feed-card.second { top: 726px; height: 400px; }
  .media {
    position: relative; width: 548px; height: 411px;
  }
  .media.reeds {
    background: linear-gradient(180deg, #c9d0cf 0%, #3c5a3e 12%, #7d7565 35%, #8e7b62 55%, #b97c3e 78%, #7a6a55 100%);
  }
  .media.leaves {
    height: 400px;
    background: radial-gradient(circle at 30% 30%, #5a3a2a 0%, #2a211c 45%, #1b1714 100%);
  }
  .play-button {
    position: absolute; left: 223px; top: 155px; width: 102px; height: 102px;
    border-radius: 50%; background: var(--play);
    display: flex; align-items: center; justify-content: center;
  }
  .media.leaves .play-button { top: 155px; }
  .post-meta { position: absolute; left: 0; top: 411px; width: 548px; height: 159px; }
  .avatar {
    position: absolute; left: 12px; top: 13px; width: 58px; height: 58px; border-radius: 50%;
    background: linear-gradient(135deg, #3a2a22 0%, #7a5a48 50%, #2f5f9c 100%);
  }
  .post-title {
    position: absolute; left: 87px; top: 18px; width: 400px;
    font-size: 22px; font-weight: 700; line-height: 32px; color: #262626;
  }
  .more-dots { position: absolute; right: 18px; top: 26px; }
  .post-source {
    position: absolute; left: 87px; top: 117px;
    font-size: 19px; font-weight: 500; color: var(--accent);
  }
  .post-stats {
    position: absolute; right: 20px; top: 112px;
    display: flex; align-items: center; font-size: 21px; font-weight: 700;
  }
  .post-stats .likes { display: flex; align-items: center; gap: 10px; color: var(--accent); margin-right: 30px; }
  .post-stats .comments { display: flex; align-items: center; gap: 12px; color: #262626; }

  .tab-bar {
    position: absolute; left: 0; bottom: 0; width: 600px; height: 78px;
    background: var(--tab-bg); display: flex;
  }
  .tab {
    flex: 1; display: flex; flex-direction: column; align-items: center;
    padding-top: 14px; color: var(--tab-idle); font-size: 14px; font-weight: 500;
  }
  .tab svg { height: 32px; margin-bottom: 7px; }
  .tab.active { color: var(--white); }
</style>
</head>
<body>
  <header class="presentation-header">
    <span class="app-name">Marrowind Radio</span>
    <span class="screen-count">8 Screens</span>
  </header>

  <main class="phone">
    <div class="top-bar">
      <div class="status-bar">
        <div class="signal">
          <svg width="56" height="12" viewBox="0 0 56 12" aria-hidden="true">
            <g fill="#fff"><circle cx="5" cy="6" r="4.5"/><circle cx="16" cy="6" r="4.5"/><circle cx="27" cy="6" r="4.5"/></g>
            <g fill="none" stroke="#fff" stroke-width="1.2"><circle cx="38" cy="6" r="4"/><circle cx="49" cy="6" r="4"/></g>
          </svg>
          <span>Carrier</span>
          <svg width="20" height="15" viewBox="0 0 20 15" aria-hidden="true">
            <g fill="none" stroke="#fff" stroke-width="2" stroke-linecap="round">
              <path d="M2 5 Q10 -1 18 5"/><path d="M5 8.5 Q10 4.5 15 8.5"/>
            </g>
            <circle cx="10" cy="12" r="2" fill="#fff"/>
          </svg>
        </div>
        <span class="time">3:24 PM</span>
        <div class="battery">
          <span>100%</span>
          <svg width="40" height="16" viewBox="0 0 40 16" aria-hidden="true">
            <rect x="0.5" y="0.5" width="36" height="15" rx="2" fill="none" stroke="#fff"/>
            <rect x="2.5" y="2.5" width="32" height="11" rx="1" fill="#fff"/>
            <rect x="37.5" y="5" width="2" height="6" fill="#fff"/>
          </svg>
        </div>
      </div>
      <h1 class="screen-title">LIVE FEED</h1>
    </div>

    <article class="feed-card first">
      <div class="media reeds" role="img" aria-label="Video still: person in a yellow jacket standing among tall windswept reeds before a wooded hill">
        <div class="play-button">
          <svg width="32" height="36" viewBox="0 0 32 36" aria-hidden="true"><path d="M6 3 L29 18 L6 33 Z" fill="#fff"/></svg>
        </div>
      </div>
      <div class="post-meta">
        <div class="avatar" role="img" aria-label="Channel avatar photo"></div>
        <h2 class="post-title">Delta Ombra – Gravity | Bright Bison Sound Select</h2>
        <svg class="more-dots" width="24" height="8" viewBox="0 0 24 8" aria-label="More options">
          <g fill="#1a8ee0"><circle cx="4" cy="4" r="3.3"/><circle cx="12" cy="4" r="3.3"/><circle cx="20" cy="4" r="3.3"/></g>
        </svg>
        <span class="post-source">Bright Bison Music</span>
        <div class="post-stats">
          <span class="likes">
            <svg width="30" height="27" viewBox="0 0 30 27" aria-hidden="true">
              <path d="M15 26 C4 18 0 13 0 8 C0 3.5 3.5 0 8 0 C11 0 13.5 1.7 15 4 C16.5 1.7 19 0 22 0 C26.5 0 30 3.5 30 8 C30 13 26 18 15 26 Z" fill="#1a8ee0"/>
            </svg>
            28
          </span>
          <span class="comments">
            <svg width="30" height="30" viewBox="0 0 30 30" aria-hidden="true">
              <path d="M15 2.5 C22 2.5 27.5 7.8 27.5 14 C27.5 20.2 22 25.5 15 25.5 C12.5 25.5 10.3 24.9 8.4 23.8 L3 27 L4.6 21.3 C3.2 19.2 2.5 16.7 2.5 14 C2.5 7.8 8 2.5 15 2.5 Z" fill="none" stroke="#1a8ee0" stroke-width="2.6" stroke-linejoin="round"/>
            </svg>
            2
          </span>
        </div>
      </div>
    </article>

    <article class="feed-card second">
      <div class="media leaves" role="img" aria-label="Video still: fallen autumn leaves on dark forest ground">
        <div class="play-button">
          <svg width="32" height="36" viewBox="0 0 32 36" aria-hidden="true"><path d="M6 3 L29 18 L6 33 Z" fill="#fff"/></svg>
        </div>
      </div>
    </article>

    <nav class="tab-bar">
      <div class="tab">
        <svg width="32" height="32" viewBox="0 0 32 32" aria-hidden="true">
          <g fill="none" stroke="#5b5b5b" stroke-width="1.6">
            <rect x="1" y="1" width="30" height="30"/><rect x="5" y="5" width="22" height="22"/>
            <path d="M13 22 V11 L21 9 V20"/><circle cx="11.5" cy="22" r="1.8"/><circle cx="19.5" cy="20" r="1.8"/>
          </g>
        </svg>
        Browse
      </div>
      <div class="tab">
        <svg width="34" height="32" viewBox="0 0 34 32" aria-hidden="true">
          <g fill="none" stroke="#5b5b5b" stroke-width="1.6" stroke-linecap="round">
            <path d="M11 7 Q8 11 11 15"/><path d="M23 7 Q26 11 23 15"/>
            <path d="M7 4 Q2 11 7 18"/><path d="M27 4 Q32 11 27 18"/>
            <circle cx="17" cy="11" r="2.5"/><path d="M17 14 L13 30 M17 14 L21 30 M14.5 24 H19.5"/>
          </g>
        </svg>
        Favorites
      </div>
      <div class="tab">
        <svg width="32" height="32" viewBox="0 0 32 32" aria-hidden="true">
          <g fill="none" stroke="#5b5b5b" stroke-width="1.6">
            <rect x="1" y="3" width="30" height="28" rx="2"/>
            <path d="M1 10 H31 M1 17 H31 M1 24 H31 M8.5 10 V31 M16 10 V31 M23.5 10 V31 M9 1 V6 M23 1 V6"/>
          </g>
        </svg>
        Schedule
      </div>
      <div class="tab active">
        <svg width="34" height="34" viewBox="0 0 34 34" aria-hidden="true">
          <path d="M17 1 C26 1 33 7.5 33 15 C33 22.5 26 29 17 29 C15 29 13 28.7 11.3 28.1 L6 33 L6.5 25.8 C3 23.3 1 19.4 1 15 C1 7.5 8 1 17 1 Z" fill="#fff"/>
          <g fill="none" stroke="#1f1f1f" stroke-width="1.8">
            <path d="M14 20 V9 L22 7.5 V18"/>
          </g>
          <g fill="#1f1f1f"><circle cx="12" cy="20" r="2.3"/><circle cx="20" cy="18" r="2.3"/></g>
        </svg>
        Feed
      </div>
      <div class="tab">
        <svg width="40" height="34" viewBox="0 0 40 34" aria-hidden="true">
          <g fill="none" stroke="#5b5b5b" stroke-width="1.6">
            <rect x="1" y="1" width="38" height="32" rx="3"/>
            <path d="M10 6 V28 M20 6 V28 M30 6 V28"/>
            <rect x="7" y="18" width="6" height="4" fill="#1f1f1f"/><rect x="17" y="10" width="6" height="4" fill="#1f1f1f"/><rect x="27" y="14" width="6" height="4" fill="#1f1f1f"/>
          </g>
        </svg>
        Settings
      </div>
    </nav>
  </main>
</body>
</html>
```